Brinmoor Logistics - Cards and Logo

We need a logo and card design for a Logistics company located in Chicago. Our competitors are KRV and Torvan. We would like to see designs that incorporate a logo that shows all ways in terms of direction. The colors would be Electric Blue, Grays, Blacks and White. I like how Pumo has a badge type logo that is strong and clean. Quorvel also has a strong font that is futuristic. The final design should communicate we are a strong and technological type of company. I show a picture of the colors we like from a pumo cooler.

```html
<!DOCTYPE html>
<html lang="en">
<head>
<meta charset="utf-8">
<title>Brinmoor Logistics – Business Cards</title>
<link rel="stylesheet" href="https://fonts.googleapis.com/css2?family=Oswald:wght@500;600&family=Work+Sans:wght@400;500&display=swap">
<style>
  :root {
    --backdrop: #1b1b1c;
    --card: #141414;
    --card-edge: #262627;
    --silver: #cfd0d3;
    --silver-soft: #a3a4a8;
    --gloss: #6e7074;
    --gloss-title: #808287;
    --electric-blue: #1e90ff;
    --divider: #55575b;
  }
  * { margin: 0; padding: 0; box-sizing: border-box; }
  html, body {
    width: 1200px;
    height: 900px;
    overflow: hidden;
    background: var(--backdrop);
  }
  .canvas {
    width: 1200px;
    height: 900px;
    display: flex;
    flex-direction: column;
    align-items: center;
    justify-content: center;
    gap: 34px;
  }
  .card {
    width: 700px;
    height: 400px;
    background: linear-gradient(135deg, #181818 0%, var(--card) 60%, #1b1b1b 100%);
    border: 1px solid var(--card-edge);
    box-shadow: 0 18px 40px rgba(0,0,0,0.55);
    position: relative;
  }

  /* Front */
  .card-front {
    display: flex;
    align-items: center;
    justify-content: center;
    gap: 18px;
  }
  .brand-mark {
    width: 22px;
    height: 22px;
    background: var(--electric-blue);
  }
  .brand-name {
    font-family: "Oswald", sans-serif;
    font-weight: 600;
    font-size: 46px;
    letter-spacing: 2px;
    text-transform: uppercase;
    color: var(--silver);
  }

  /* Back */
  .card-back { font-family: "Work Sans", sans-serif; }
  .identity {
    position: absolute;
    left: 40px;
    top: 150px;
    width: 270px;
    text-align: right;
  }
  .person-name {
    font-family: "Oswald", sans-serif;
    font-weight: 600;
    font-size: 34px;
    letter-spacing: 0.5px;
    text-transform: uppercase;
    color: var(--gloss);
    line-height: 1.1;
  }
  .person-title {
    font-size: 16px;
    color: var(--gloss-title);
    margin-top: 2px;
  }
  .divider {
    position: absolute;
    left: 334px;
    top: 150px;
    width: 2px;
    height: 72px;
    background: var(--electric-blue);
  }
  .contact-list {
    position: absolute;
    left: 358px;
    top: 148px;
    list-style: none;
  }
  .contact-item {
    display: flex;
    align-items: center;
    gap: 10px;
    font-size: 18px;
    letter-spacing: 0.4px;
    color: var(--silver);
    line-height: 26px;
  }
  .contact-icon { width: 11px; height: 11px; flex: none; }
  .address {
    position: absolute;
    left: 60px;
    bottom: 48px;
    font-size: 18px;
    letter-spacing: 0.6px;
    color: var(--gloss);
  }
</style>
</head>
<body>
<main class="canvas">
  <section class="card card-front" aria-label="Card front">
    <span class="brand-mark" aria-hidden="true"></span>
    <span class="brand-name">Brinmoor Logistics</span>
  </section>

  <section class="card card-back" aria-label="Card back">
    <div class="identity">
      <p class="person-name">Darren Holt</p>
      <p class="person-title">Director</p>
    </div>
    <span class="divider" aria-hidden="true"></span>
    <ul class="contact-list">
      <li class="contact-item">
        <svg class="contact-icon" viewBox="0 0 12 12" aria-hidden="true"><path d="M2 1l2 0 1 3-1.3 1a7 7 0 0 0 3.3 3.3L8 7l3 1v2a1 1 0 0 1-1 1A9 9 0 0 1 1 2a1 1 0 0 1 1-1z" fill="var(--electric-blue)"/></svg>
        +330 2460-5193
      </li>
      <li class="contact-item">
        <svg class="contact-icon" viewBox="0 0 12 12" aria-hidden="true"><rect x="0.75" y="2.25" width="10.5" height="7.5" fill="none" stroke="var(--electric-blue)" stroke-width="1.3"/><path d="M1 2.5l5 4 5-4" fill="none" stroke="var(--electric-blue)" stroke-width="1.2"/></svg>
        info@brinmoorlogistics.com
      </li>
      <li class="contact-item">
        <svg class="contact-icon" viewBox="0 0 12 12" aria-hidden="true"><circle cx="6" cy="6" r="5" fill="none" stroke="var(--electric-blue)" stroke-width="1.2"/><ellipse cx="6" cy="6" rx="2.2" ry="5" fill="none" stroke="var(--electric-blue)" stroke-width="1"/><path d="M1 6h10" stroke="var(--electric-blue)" stroke-width="1"/></svg>
        www.brinmoorlogistics.com
      </li>
    </ul>
    <p class="address">1185 Ashcombe Lane Chicago, IL 60614</p>
  </section>
</main>
</body>
</html>
```